Business Card Bright Willow Path
Professional
Marla Quennby, ACC, MSc, DipC
Founder
HTMA Administration Office
PO Box 27381
Birmingham
B47 3KT
info@brightwillowpath.co.uk
brightwillowpath.co.uk
Please use both variations of the logo while submitting design.
Business cards to look modern, fresh, feminine, in alignment with logo branding.
Small print to say: a division of The Harbor Trust For Mentoring Ambition
Colour scheme, images and writting to co ordinate with logo.
I do not want the address on the business cards
The market for these cards is proffessional women hence a modern, proffessional yet not too corporate and not "woo woo".
I do not want the address on the business cards.

```html
<!DOCTYPE html>
<html lang="en">
<head>
<meta charset="UTF-8">
<title>Bright Willow Path – Business Card</title>
<link rel="stylesheet" href="https://fonts.googleapis.com/css2?family=Open+Sans:wght@400;600;700&display=swap">
<style>
  :root {
    --page-bg: #ecebe8;
    --card-bg: #ffffff;
    --leaf-green: #6f9a3e;
    --olive: #8a7d45;
    --ink: #4d4d4d;
    --divider: #8a8a8a;
  }
  * { box-sizing: border-box; margin: 0; padding: 0; }
  html, body {
    width: 1200px; height: 914px; overflow: hidden;
    background: var(--page-bg);
    font-family: "Open Sans", Arial, sans-serif;
  }
  .card {
    position: absolute;
    left: 100px; top: 171px;
    width: 1000px; height: 572px;
    background: var(--card-bg);
    box-shadow: 0 10px 30px rgba(0,0,0,0.12);
    overflow: hidden;
  }
  .brand {
    position: absolute;
    left: 50px; top: 150px;
    width: 460px;
    text-align: center;
  }
  .brand-mark {
    width: 74px; height: 74px;
    margin: 0 auto 22px;
    border-radius: 50%;
    background: var(--leaf-green);
  }
  .brand-name {
    font-size: 44px;
    font-weight: 400;
    color: var(--leaf-green);
    letter-spacing: -0.5px;
    line-height: 1;
    white-space: nowrap;
  }
  .brand-tagline {
    margin-top: 10px;
    font-size: 13.5px;
    color: var(--leaf-green);
    white-space: nowrap;
  }
  .divider {
    position: absolute;
    left: 530px; top: 168px;
    width: 1px; height: 212px;
    background: var(--divider);
  }
  .contact {
    position: absolute;
    left: 555px; top: 160px;
    color: var(--ink);
  }
  .person-name {
    font-size: 22px;
    font-weight: 600;
    color: var(--leaf-green);
    line-height: 1.2;
  }
  .person-role {
    font-size: 16px;
    margin: 4px 0 22px;
    color: var(--ink);
  }
  .contact-list { list-style: none; }
  .contact-list li {
    display: flex; align-items: center;
    font-size: 16px;
    line-height: 1;
    margin-bottom: 9px;
    white-space: nowrap;
  }
  .contact-icon {
    width: 18px; height: 18px;
    margin-right: 10px;
    flex: none;
  }
  .band {
    position: absolute;
    left: 0; bottom: 0;
    width: 1000px; height: 96px;
  }
</style>
</head>
<body>
  <main class="card">
    <section class="brand">
      <div class="brand-mark"></div>
      <div class="brand-name">Bright Willow Path</div>
      <div class="brand-tagline">Renew your mind, restore your balance and grow your calm</div>
    </section>

    <div class="divider"></div>

    <section class="contact">
      <div class="person-name">Marla Quennby,<br>ACC, MSc, DipC</div>
      <div class="person-role">Founder</div>
      <ul class="contact-list">
        <li>
          <svg class="contact-icon" viewBox="0 0 18 18" aria-hidden="true">
            <circle cx="9" cy="9" r="9" fill="var(--olive)"/>
            <path d="M6 4.5 L7.6 4.5 L8.3 6.8 L7.2 7.7 Q8 9.8 10.3 10.8 L11.2 9.7 L13.5 10.4 L13.5 12 Q12.6 13.5 10.8 13 Q6.2 11.5 5 7 Q4.6 5.2 6 4.5 Z" fill="#fff"/>
          </svg>
          +44 (0) 845 000 2716
        </li>
        <li>
          <svg class="contact-icon" viewBox="0 0 18 18" aria-hidden="true">
            <circle cx="9" cy="9" r="9" fill="var(--olive)"/>
            <rect x="6.2" y="3.8" width="5.6" height="10.4" rx="1" fill="#fff"/>
            <rect x="7" y="5" width="4" height="6.5" fill="var(--olive)"/>
          </svg>
          +44 (0) 7700 90 04 58
        </li>
        <li>
          <svg class="contact-icon" viewBox="0 0 18 18" aria-hidden="true">
            <circle cx="9" cy="9" r="9" fill="var(--olive)"/>
            <rect x="4.5" y="5.8" width="9" height="6.4" fill="#fff"/>
            <path d="M4.5 5.8 L9 9.4 L13.5 5.8" fill="none" stroke="var(--olive)" stroke-width="0.9"/>
          </svg>
          info@brightwillowpath.co.uk
        </li>
        <li>
          <svg class="contact-icon" viewBox="0 0 18 18" aria-hidden="true">
            <circle cx="9" cy="9" r="9" fill="var(--olive)"/>
            <circle cx="9" cy="9" r="4.6" fill="none" stroke="#fff" stroke-width="1"/>
            <ellipse cx="9" cy="9" rx="2" ry="4.6" fill="none" stroke="#fff" stroke-width="1"/>
            <line x1="4.4" y1="9" x2="13.6" y2="9" stroke="#fff" stroke-width="1"/>
          </svg>
          www.brightwillowpath.co.uk
        </li>
      </ul>
    </section>

    <svg class="band" viewBox="0 0 1000 96" preserveAspectRatio="none" aria-hidden="true">
      <polygon points="0,26 620,26 650,96 0,96" fill="var(--leaf-green)"/>
      <polygon points="620,26 1000,26 1000,96 650,96" fill="var(--olive)"/>
      <line x1="620" y1="26" x2="650" y2="96" stroke="#fff" stroke-width="4"/>
    </svg>
  </main>
</body>
</html>
```